Lofty Intake needs a 8.5" X 11" flyer to give to college presidents

We need a flyer design for Lofty Intake that briefly explains what we do and encourages college presidents to give the flyer to their directors of admission. Please be consistent with our brand www.loftyintake.example. I've attached an example of a cool three dimensional flyer that I like...but I'm open to all ideas.

FRONT: The first on-line and fully automated recruiting tool that allows admissions officers to electronically contact high school seniors and send them invitations to apply that include estimates of merit aid.

BACK: Lofty Intake brings your college or university students' mobile devices and desktops. Knowing their credentials, admissions offers can send either a single student or groups of students invitations to apply that include offers of merit aid. Your school’s invitation is a recruiting document that appeals to students and parents with a clear price signal, and to students and counselors with customizable links to your college or universities website, rankings, social media and any particular information or commendation.

For information about how Lofty Intake fits into your enrollment strategy and expands your access to students, families and counselors, please contact us by phone 866.519.2274 or email admin@loftyintake.example. An on-line presentation of Lofty Intake takes less than 30 minutes.

college presidents and admissions officers

Education

• front and back designs
• a look of depth or three dimensions

```html
<!DOCTYPE html>
<html lang="en">
<head>
<meta charset="utf-8">
<title>Lofty Intake Flyer – Front and Back</title>
<link href="https://fonts.googleapis.com/css2?family=Alfa+Slab+One&family=Arimo:wght@400;700&display=swap" rel="stylesheet">
<style>
  :root {
    --navy: #0f2a47;
    --red: #8f1d21;
    --white: #ffffff;
    --ink: #1b2a3d;
    --device: #121212;
    --backdrop: #e4e4e2;
    --slab: "Alfa Slab One", Georgia, serif;
    --sans: "Arimo", Arial, sans-serif;
  }
  * { box-sizing: border-box; margin: 0; padding: 0; }
  html, body { width: 1200px; height: 1200px; overflow: hidden; }
  body { background: var(--backdrop); font-family: var(--sans); position: relative; }

  .flyer {
    position: absolute;
    top: 264px;
    width: 520px;
    height: 673px;
    overflow: hidden;
    background: var(--navy);
  }
  .flyer--front { left: 50px; }
  .flyer--back { left: 630px; }

  /* Front */
  .front-header {
    position: absolute; left: 0; top: 0; width: 100%; height: 150px;
    background: var(--white);
  }
  .brand-name {
    font-family: var(--slab);
    color: var(--navy);
    text-align: center;
    line-height: 1;
    letter-spacing: 1px;
  }
  .front-header .brand-name {
    position: absolute; left: 0; right: 0; top: 58px; font-size: 56px;
  }
  .hero-photo {
    position: absolute; left: 58px; top: 178px; width: 404px; height: 250px;
    background: linear-gradient(160deg, #c9d6e3 0%, #8a9bb0 35%, #2a3240 70%, #14181f 100%);
    box-shadow: 0 0 18px rgba(255,255,255,0.35);
  }
  .headline-band {
    position: absolute; left: 0; top: 448px; width: 100%; height: 104px;
    background: var(--red);
    display: flex; align-items: center; justify-content: center;
  }
  .headline {
    font-family: var(--slab);
    font-weight: 400;
    color: var(--white);
    font-size: 24px;
    line-height: 1.3;
    text-align: center;
    text-transform: uppercase;
    letter-spacing: 0.5px;
  }
  .front-body {
    position: absolute; left: 36px; right: 36px; top: 574px;
    color: var(--white);
    font-size: 16.5px;
    line-height: 1.4;
    text-align: center;
  }

  /* Back */
  .device {
    position: absolute; left: 48px; top: 22px; width: 424px; height: 720px;
    background: var(--device);
    border-radius: 46px;
  }
  .device-speaker {
    position: absolute; left: 50%; top: 26px; width: 80px; height: 18px;
    margin-left: -40px; border: 2px solid #444; border-radius: 9px; background: #1d1d1d;
  }
  .device-screen {
    position: absolute; left: 22px; right: 22px; top: 70px; bottom: 0;
    background: var(--white);
  }
  .status-bar {
    display: flex; justify-content: space-between; align-items: center;
    padding: 8px 12px 0; font-size: 12px; color: #000;
  }
  .status-signal { letter-spacing: 1px; font-size: 12px; }
  .status-battery { display: flex; align-items: center; gap: 4px; }
  .battery { width: 22px; height: 10px; background: #000; border-radius: 2px; }
  .device-screen .brand-name {
    margin-top: 46px; font-size: 46px;
  }
  .intro {
    margin: 36px 16px 0; font-size: 11.5px; line-height: 1.3; color: var(--ink);
  }
  .invitation {
    position: absolute; left: 16px; top: 262px; width: 172px;
    font-size: 13px; font-weight: 700; line-height: 1.35; color: var(--ink);
  }
  .presentation-badge {
    position: absolute; right: 6px; top: 258px; width: 180px; height: 180px;
    border: 2px solid var(--red); border-radius: 50%;
    display: flex; align-items: center; justify-content: center;
    font-family: var(--slab); color: var(--red);
    font-size: 12px; line-height: 1.2; text-align: center; text-transform: uppercase;
    background: var(--white);
  }
  .contact-band {
    position: absolute; left: 0; top: 540px; width: 100%; height: 106px;
    background: var(--red); color: var(--white); text-align: center;
    padding-top: 16px;
  }
  .contact-intro { font-size: 15px; line-height: 1.3; }
  .contact-details { font-size: 18px; font-weight: 700; margin-top: 4px; }
  .contact-details span { font-weight: 400; }
</style>
</head>
<body>

<section class="flyer flyer--front" aria-label="Flyer front">
  <header class="front-header">
    <div class="brand-name">Lofty Intake</div>
  </header>
  <div class="hero-photo" role="img" aria-label="Photo of smiling graduates in caps and gowns celebrating outdoors"></div>
  <div class="headline-band">
    <h1 class="headline">The first on-line and fully<br>automated recruiting tool</h1>
  </div>
  <p class="front-body">that allows admissions officers to electronically contact<br>high school seniors and send them invitations to<br>apply that include estimates of merit aid.</p>
</section>

<section class="flyer flyer--back" aria-label="Flyer back">
  <div class="device">
    <div class="device-speaker"></div>
    <div class="device-screen">
      <div class="status-bar">
        <span class="status-signal">●●●●●</span>
        <span>9:41 AM</span>
        <span class="status-battery">100% <span class="battery"></span></span>
      </div>
      <div class="brand-name">Lofty Intake</div>
      <p class="intro">Lofty Intake brings your college or university to high school seniors’ mobile devices. Knowing students’ credentials, admissions officers select a single student or groups of students to receive your invitation to apply.</p>
      <p class="invitation">Your school’s invitation is a custom recruiting document that sends a clear price signal to students and parents and links to your website, social media, rankings and commendations you’d like students to know about.</p>
      <div class="presentation-badge">An on-line<br>presentation of<br>Lofty Intake<br>takes less than<br>30 minutes.</div>
    </div>
  </div>
  <div class="contact-band">
    <p class="contact-intro">For information about how Lofty Intake fits<br>into your enrollment strategy please contact us on:</p>
    <p class="contact-details">866.519.2274 <span>or</span> admin@loftyintake.example</p>
  </div>
</section>

</body>
</html>
```